Trade Show Banner

Looking for a design for 36" x 90" stretched fabric display.
Commercial construction company, can include Chicago high rise buildings, blue prints, steel studs.
List of types of work should include:
Commercial office build-out
Hospital expansion
Educational and institutional
Laboratory and research
Dental and medical office
Veterinary Clinics

website brolmerconstruction.com

Target Market(s)

Architects and General Contractors

Industry/Entity Type

Commercial Construction

Colors
0054AA
0677BA
7BADD7
CADEEF
E8F1F8

Requirements
Must have
• Our logo, blueprints, chicago high rise
Should not have
• no cartoon construction logos, no houses

```html
<!DOCTYPE html>
<html lang="en">
<head>
<meta charset="utf-8">
<title>Brolmer Construction – Trade Show Banner</title>
<link rel="stylesheet" href="https://fonts.googleapis.com/css2?family=Montserrat:wght@400;800&family=Roboto+Condensed:wght@300&display=swap">
<style>
  :root {
    --brand-deep: #0054AA;
    --brand-mid: #0677BA;
    --brand-light: #7BADD7;
    --brand-pale: #CADEEF;
    --brand-mist: #E8F1F8;
    --white: #ffffff;
    --sky: #e9ebee;
    --steel-dark: #1b2026;
    --steel-mid: #5a6370;
  }
  * { margin: 0; padding: 0; box-sizing: border-box; }
  html, body { width: 1200px; height: 3007px; overflow: hidden; background: var(--white); }
  .banner { position: relative; width: 1200px; height: 3007px; overflow: hidden; background: var(--white); }

  .brand-header { position: absolute; left: 0; top: 0; width: 1200px; height: 430px; display: flex; align-items: center; justify-content: center; gap: 36px; }
  .brand-square { width: 150px; height: 150px; background: var(--brand-deep); flex: none; }
  .brand-name { font-family: "Montserrat", sans-serif; font-weight: 800; color: var(--brand-deep); font-size: 78px; line-height: 1.02; letter-spacing: 2px; text-transform: uppercase; }

  .skyline-photo { position: absolute; left: 0; top: 432px; width: 1200px; height: 805px;
    background:
      radial-gradient(ellipse 260px 420px at 52% 12%, var(--sky) 0%, rgba(233,235,238,0.6) 55%, rgba(233,235,238,0) 100%),
      linear-gradient(90deg, var(--steel-dark) 0%, var(--steel-mid) 30%, #9aa1aa 50%, var(--steel-mid) 70%, var(--steel-dark) 100%); }

  .services-panel { position: absolute; left: 0; top: 1237px; width: 1200px; height: 1770px;
    background: linear-gradient(160deg, #2f86d6 0%, var(--brand-mid) 30%, #1a72c2 60%, var(--brand-deep) 100%); }
  .blueprint-art { position: absolute; inset: 0;
    background: radial-gradient(ellipse 520px 900px at 15% 40%, rgba(123,173,215,0.35) 0%, rgba(123,173,215,0) 100%); }

  .service-list { position: absolute; right: 64px; top: 1440px; list-style: none; text-align: right;
    font-family: "Roboto Condensed", sans-serif; font-weight: 300; color: var(--white); font-size: 90px; line-height: 1; }
  .service-list li { height: 169px; white-space: nowrap; }
  .service-list li::before { content: "• "; }

  .website { position: absolute; right: 66px; top: 2896px; font-family: "Montserrat", sans-serif; font-weight: 400; font-size: 47px; color: var(--white); letter-spacing: 0.5px; }
</style>
</head>
<body>
<main class="banner">
  <header class="brand-header">
    <div class="brand-square"></div>
    <div class="brand-name">Brolmer<br>Construction</div>
  </header>

  <div class="skyline-photo" role="img" aria-label="Photograph looking up at Chicago glass high-rise towers against a pale sky"></div>

  <section class="services-panel">
    <div class="blueprint-art" role="img" aria-label="Faint white blueprint drawing lines over blue background"></div>
  </section>

  <ul class="service-list">
    <li>Commercial office build-out</li>
    <li>Hospital expansion</li>
    <li>Educational and institutional</li>
    <li>Laboratory and research</li>
    <li>Dental and medical office</li>
    <li>Veterinary Clinics</li>
  </ul>

  <p class="website">brolmerconstruction.com</p>
</main>
</body>
</html>
```